Simple, Professional and neat business card design for Vendralo Inc.

We're looking to re-vamp our business card design. We're a supplier of innovative feed ingredients for the North American animal agriculture industry. We are located in Lucknow, Ontario, Canada and our flagship product is a product that prevents milk fever in dairy cows when the calve, it is fed before calving and is very effective compared to other alternatives available on the market today.

Our company has Danish roots and we import all of our product from our Danish partner/manufacturer in Denmark. We like our design to embrace high professionalism while remaining neat and simple.

Target Market(s)

B2B, Feed Mills, Veterinary Clinics, Large integrators/producers,

Industry/Entity Type

Agribusiness

Contact Information for Business Card

We like the rounded corners because they make the card easy to sit in a wallet and not many use it so it makes the card stand out, just possibly something to take account for during the design.

As you can also see on the sliders below, looking for a that simple but proffesional scandinavian design.

Requirements
Nice to have
• Rounded corners
Should not have
• Too vibrant

```html
<!DOCTYPE html>
<html lang="en">
<head>
<meta charset="utf-8">
<title>Vendralo Inc. business card</title>
<link href="https://fonts.googleapis.com/css2?family=Lato:wght@300;400;700;900&display=swap" rel="stylesheet">
<style>
  :root {
    --page: #e9eaec;
    --card: #ffffff;
    --blue: #1b56a8;
    --ink: #2a2a2a;
    --rule: #555a60;
    --grey: #8d8f92;
  }
  * { margin: 0; padding: 0; box-sizing: border-box; }
  html, body { width: 1200px; height: 1200px; overflow: hidden; background: var(--page); font-family: "Lato", sans-serif; }
  .canvas { position: relative; width: 1200px; height: 1200px; }
  .card {
    position: absolute; left: 150px; width: 900px; height: 514px;
    background: var(--card); border-radius: 34px; overflow: hidden;
    box-shadow: 0 10px 30px rgba(0,0,0,.12);
  }
  .card-back { top: 50px; }
  .card-front { top: 626px; }

  /* back */
  .back-mark {
    position: absolute; top: 150px; left: 0; width: 100%;
    display: flex; justify-content: center; align-items: center; gap: 18px;
  }
  .mark-dot { width: 34px; height: 34px; border-radius: 50%; background: var(--blue); }
  .mark-name { font-size: 58px; font-weight: 700; color: var(--blue); letter-spacing: 1px; }
  .back-web {
    position: absolute; top: 330px; left: 0; width: 100%;
    display: flex; align-items: center; gap: 28px; padding: 0 0;
  }
  .back-web .rule { flex: 1; height: 1px; background: var(--rule); }
  .back-web .url { font-size: 26px; font-weight: 300; color: var(--ink); letter-spacing: 1px; }

  /* front */
  .brand {
    position: absolute; left: 50px; top: 70px; width: 400px; text-align: center;
  }
  .brand-mark { display: flex; justify-content: center; align-items: center; gap: 12px; margin-bottom: 40px; }
  .brand-mark .mark-dot { width: 24px; height: 24px; }
  .brand-mark .mark-name { font-size: 40px; }
  .company { font-size: 52px; font-weight: 900; color: var(--blue); letter-spacing: 1px; }
  .divider { position: absolute; left: 470px; top: 60px; width: 1.5px; height: 300px; background: var(--blue); }
  .contact { position: absolute; left: 510px; top: 58px; width: 370px; color: var(--ink); }
  .person { font-size: 32px; font-weight: 900; color: var(--blue); margin-bottom: 24px; letter-spacing: .5px; }
  .line { font-size: 20px; line-height: 29px; }
  .line .label { color: var(--blue); }
  .group { margin-bottom: 14px; }
  .social { display: flex; gap: 18px; margin-top: 10px; }
  .social span { font-size: 15px; font-weight: 700; color: var(--blue); }
  .address-band { position: absolute; left: 0; bottom: 0; width: 100%; height: 96px; }
  .address {
    position: absolute; left: 40px; bottom: 44px;
    display: flex; align-items: center; gap: 14px;
    color: #fff; font-size: 22px; letter-spacing: .5px;
  }
</style>
</head>
<body>
<div class="canvas">

  <section class="card card-back">
    <div class="back-mark">
      <span class="mark-dot"></span>
      <span class="mark-name">Vendralo</span>
    </div>
    <div class="back-web">
      <span class="rule"></span>
      <span class="url">www.vendralo.com</span>
      <span class="rule"></span>
    </div>
  </section>

  <section class="card card-front">
    <div class="brand">
      <div class="brand-mark">
        <span class="mark-dot"></span>
        <span class="mark-name">Vendralo</span>
      </div>
      <div class="company">VENDRALO INC.</div>
    </div>
    <div class="divider"></div>
    <div class="contact">
      <div class="person">MIKKEL SØRVANG</div>
      <div class="group">
        <div class="line"><span class="label">Mobile:</span> 519 .555 .0147</div>
        <div class="line"><span class="label">Office:</span> 519 .555 .0192</div>
      </div>
      <div class="group">
        <div class="line"><span class="label">Toll Free:</span> 888 .555 .0168</div>
        <div class="line"><span class="label">Fax:</span> 519 .555 .0173</div>
      </div>
      <div class="group">
        <div class="line"><span class="label">Email:</span> mikkel@vendralo.com</div>
        <div class="line"><span class="label">Web:</span> www.vendralo.com</div>
      </div>
      <div class="social">
        <span>Socialbook</span><span>Chirper</span><span>Viewtube</span>
      </div>
    </div>
    <svg class="address-band" viewBox="0 0 900 96" preserveAspectRatio="none" aria-hidden="true">
      <path d="M380 96 L380 70 Q380 40 410 40 L900 40 L900 96 Z" fill="var(--grey)"/>
      <path d="M0 96 L0 20 L620 20 Q640 20 636 40 L626 96 Z" fill="var(--blue)"/>
    </svg>
    <div class="address">
      <svg width="18" height="24" viewBox="0 0 18 24" aria-hidden="true">
        <path d="M9 0C4 0 0 4 0 9c0 7 9 15 9 15s9-8 9-15c0-5-4-9-9-9z" fill="#fff"/>
        <circle cx="9" cy="9" r="3.5" fill="var(--blue)"/>
      </svg>
      <span>Box 412, Arnholt, Ontario Canada N0H 3K1</span>
    </div>
  </section>

</div>
</body>
</html>
```